Brolga Ridge Earthmoving & Transport Business Card

Can you please design a business card for an Earthworks, Haulage truck and machinery hire company. They also provide sand soil and mulch supply, as well as screening of products. Can you re-create the logo from the attached but add Brolga Ridge Earthmoving & Transport just use the three diamond design.

Target Market(s)

Earthmoving and Transport, Landscapers, Construction

Contact Information for Business Card

ABN 52 907 338 214, Dale Pettigrew, Managing Director, Brolga Ridge Earthmoving & Transport Mobile 0438 256 904 Email brgtransport2011@haulmail.example

Font styles to use
Sans Serif

Colors
ec1f27
000000
cbcbcb
ffffff

Requirements
Must have
• Listed on the back, Earthworks | Haulage | Truck and Machinery Hire | Sand, Soil & Mulch Supply | Screening of Products
Nice to have
• Would be good for it to look appealing to a mans man, because it relates to heavy machinery, earthworks, construction etc. Black, red and white would be good maybe with a bit of silver somewhere.
Should not have
• not sure

```html
<!DOCTYPE html>
<html lang="en">
<head>
<meta charset="utf-8">
<title>Brolga Ridge Earthmoving &amp; Transport – Business Card</title>
<link rel="stylesheet" href="https://fonts.googleapis.com/css2?family=Montserrat:ital,wght@0,800;1,500&family=Arimo:wght@400;700&display=swap">
<style>
  :root {
    --red: #ec1f27;
    --black: #000000;
    --ink: #111111;
    --silver: #cbcbcb;
    --white: #ffffff;
    --stage: #1d1d1f;
  }
  * { box-sizing: border-box; margin: 0; padding: 0; }
  html, body { width: 1200px; height: 1200px; overflow: hidden; }
  body {
    background: var(--stage);
    display: flex;
    flex-direction: column;
    align-items: center;
    justify-content: center;
    gap: 56px;
    font-family: "Arimo", Arial, sans-serif;
  }
  .card {
    width: 900px;
    height: 514px;
    position: relative;
    overflow: hidden;
  }

  /* ---------- back ---------- */
  .card-back {
    display: flex;
    border-radius: 0 56px 0 56px;
    background: var(--white);
  }
  .services {
    width: 52%;
    background: var(--ink);
    padding: 62px 0 0 72px;
    list-style: none;
  }
  .service {
    display: flex;
    align-items: center;
    gap: 30px;
    height: 78px;
    font-family: "Montserrat", sans-serif;
    font-style: italic;
    font-weight: 500;
    font-size: 23px;
    color: var(--white);
  }
  .service-icon {
    width: 34px;
    height: 28px;
    border-radius: 4px;
    background: var(--red);
    flex: none;
  }
  .back-brand {
    flex: 1;
    display: flex;
    align-items: center;
    justify-content: center;
    padding: 0 40px;
  }

  /* ---------- brand name ---------- */
  .brand {
    display: flex;
    align-items: center;
    gap: 16px;
  }
  .brand-square {
    width: 34px;
    height: 34px;
    background: var(--red);
    flex: none;
  }
  .brand-name {
    font-family: "Montserrat", sans-serif;
    font-weight: 800;
    color: var(--black);
    text-transform: uppercase;
    line-height: 1.12;
    letter-spacing: 0.5px;
  }
  .back-brand .brand-name { font-size: 25px; }

  /* ---------- front ---------- */
  .card-front {
    border-radius: 56px 0 56px 0;
    background: linear-gradient(100deg, #e9e9e9 0%, #f7f7f7 40%, var(--white) 100%);
  }
  .front-brand {
    position: absolute;
    left: 56px;
    top: 156px;
    width: 360px;
  }
  .front-brand .brand-name { font-size: 30px; }
  .divider {
    position: absolute;
    left: 436px;
    top: 96px;
    width: 2px;
    height: 250px;
    background: var(--ink);
  }
  .contact {
    position: absolute;
    left: 470px;
    right: 36px;
    top: 100px;
    color: var(--black);
    font-size: 19px;
    line-height: 1.3;
  }
  .contact-name {
    font-family: "Montserrat", sans-serif;
    font-weight: 800;
    font-size: 32px;
    line-height: 1.1;
  }
  .contact-title { color: var(--red); font-size: 24px; margin-bottom: 2px; }
  .contact-abn { margin-bottom: 14px; }
  .contact-address { margin-bottom: 14px; }
  .contact-line {
    display: flex;
    align-items: center;
    gap: 12px;
    height: 34px;
    white-space: nowrap;
  }
  .contact-line svg { width: 26px; height: 26px; flex: none; }
  .stripes {
    position: absolute;
    left: 0;
    right: 0;
    bottom: 46px;
    height: 26px;
  }
  .stripe-black {
    position: absolute;
    left: 0;
    top: 0;
    width: 52%;
    height: 14px;
    background: var(--ink);
  }
  .stripe-red {
    position: absolute;
    left: 52%;
    right: 0;
    top: 6px;
    height: 20px;
    background: var(--red);
  }
  .stripe-silver {
    position: absolute;
    left: 0;
    width: 52%;
    top: 18px;
    height: 3px;
    background: var(--silver);
  }
</style>
</head>
<body>

  <section class="card card-back">
    <ul class="services">
      <li class="service"><span class="service-icon" role="img" aria-label="Excavator icon"></span>Earthworks</li>
      <li class="service"><span class="service-icon" role="img" aria-label="Truck icon"></span>Haulage</li>
      <li class="service"><span class="service-icon" role="img" aria-label="Crane truck icon"></span>Truck and Machinery Hire</li>
      <li class="service"><span class="service-icon" role="img" aria-label="Shovel and soil pile icon"></span>Sand, Soil &amp; Mulch Supply</li>
      <li class="service"><span class="service-icon" role="img" aria-label="Screening gear icon"></span>Screening of Products</li>
    </ul>
    <div class="back-brand">
      <div class="brand">
        <span class="brand-square"></span>
        <span class="brand-name">Brolga Ridge<br>Earthmoving<br>&amp; Transport</span>
      </div>
    </div>
  </section>

  <section class="card card-front">
    <div class="front-brand">
      <div class="brand">
        <span class="brand-square"></span>
        <span class="brand-name">Brolga Ridge<br>Earthmoving<br>&amp; Transport</span>
      </div>
    </div>

    <div class="divider"></div>

    <div class="contact">
      <p class="contact-name">Dale Pettigrew</p>
      <p class="contact-title">Managing Director</p>
      <p class="contact-abn">ABN 52 907 338 214</p>
      <p class="contact-address">27 Corella Court<br>Wandoo 6031, Perth, WA</p>
      <p class="contact-line">
        <svg viewBox="0 0 26 26" aria-hidden="true">
          <rect x="4" y="4" width="18" height="18" rx="3" transform="rotate(45 13 13)" fill="var(--red)"/>
          <path d="M10 8.5c.6-.5 1.3-.3 1.6.3l.8 1.6c.2.5 0 1-.4 1.3l-.7.5c.5 1.2 1.3 2 2.5 2.5l.5-.7c.3-.4.8-.6 1.3-.4l1.6.8c.6.3.8 1 .3 1.6l-.8.9c-3.3.3-7.3-3.7-7-7z" fill="var(--white)"/>
        </svg>
        0438 256 904
      </p>
      <p class="contact-line">
        <svg viewBox="0 0 26 26" aria-hidden="true">
          <rect x="4" y="4" width="18" height="18" rx="3" transform="rotate(45 13 13)" fill="var(--red)"/>
          <rect x="8" y="9.5" width="10" height="7" fill="none" stroke="var(--white)" stroke-width="1.3"/>
          <path d="M8 9.5l5 4 5-4" fill="none" stroke="var(--white)" stroke-width="1.3"/>
        </svg>
        brgtransport2011@haulmail.example
      </p>
    </div>

    <div class="stripes">
      <span class="stripe-black"></span>
      <span class="stripe-silver"></span>
      <span class="stripe-red"></span>
    </div>
  </section>

</body>
</html>
```